Dialwell Hub
Web site
Project: Dialwell Hub
Dialwell Hub  - Telecommunications
Creative Brief
Telecommunications
Dialwell hub provides a hosted IVR(Integrated voice response) system for businesses. Think of when you call your credit card company and they ask you to enter your cc number, then they read you your balance, or let you select what you are calling about. That is what we provide. In addition, we provide automated calling solutions for companies who need to notify hundreds or thousands of people via phone or SMS text about topics (all opt-in). We are very much a web 2.0 saas company
I like www.pathmoxie.example website, www.safevane.example, tradeorbit.example, tallyfern.example. Corvix.example and quadrel.example are two big competitors. Looking very much for sass web2.0 look and feel.
green
white or grey
below header
pathmoxie.example
corvix.example
safevane.example
Pages on the site will be home, about us, contact us, products, services I am looking for both a home page and inside page design

```html
<!DOCTYPE html>
<html lang="en">
<head>
<meta charset="utf-8">
<title>Dialwell Hub – Hosted IVR</title>
<link href="https://fonts.googleapis.com/css2?family=Arimo:wght@400;700&family=Archivo+Narrow:wght@400;700&display=swap" rel="stylesheet">
<style>
:root{
  --orange:#f07d12;
  --orange-dark:#d8640a;
  --gold:#ffb43a;
  --blue:#1e8fd8;
  --blue-deep:#0f6bb5;
  --sky:#5fb8ee;
  --navy:#0b4f8a;
  --ink:#333;
  --grey:#777;
  --line:#d9d9d9;
  --white:#fff;
}
*{margin:0;padding:0;box-sizing:border-box}
html,body{width:1200px;height:1052px;overflow:hidden;background:var(--white)}
body{font-family:"Arimo",Arial,sans-serif;color:var(--ink);position:relative}
.wrap{position:absolute;left:130px;width:940px}

/* header */
.header{top:0;height:129px}
.brand{position:absolute;left:10px;top:42px;display:flex;align-items:center;gap:12px}
.brand-dot{width:40px;height:40px;border-radius:50%;background:var(--orange)}
.brand-name{font-size:30px;font-weight:700;color:var(--navy)}
.utility{position:absolute;right:0;top:6px;display:flex;align-items:center;gap:6px;font-size:11px;color:var(--grey)}
.utility input{width:100px;height:16px;border:1px solid var(--line)}
.utility .go{width:16px;height:16px;background:#666}
.callout{position:absolute;right:0;top:80px;text-align:right;font-family:"Archivo Narrow",sans-serif}
.callout .label{font-size:22px;color:var(--orange)}
.callout .label b{color:var(--blue-deep)}

/* nav */
.nav{position:absolute;left:0;top:129px;width:1200px;height:53px;background:linear-gradient(var(--orange),var(--orange-dark))}
.nav ul{position:absolute;left:140px;top:0;display:flex;list-style:none}
.nav li{color:var(--white);font-size:16px;width:130px;line-height:53px;text-align:center;border-right:1px solid rgba(255,255,255,.35)}
.nav li:first-child{width:80px;text-align:left}
.nav .search{position:absolute;right:130px;top:14px;width:200px;height:26px;background:var(--white);font-size:11px;color:#999;padding:6px 8px;border-radius:2px}

/* hero */
.hero{position:absolute;left:0;top:182px;width:1200px;height:418px;background:linear-gradient(#1b84cf,var(--sky) 62%,#cfeaf9 88%,var(--white))}
.device{position:absolute;left:150px;top:60px;width:380px;height:290px;border-radius:18px;background:linear-gradient(#4a4a4a,#151515)}
.hero-copy{position:absolute;left:652px;top:56px;width:530px;color:var(--white);font-family:"Archivo Narrow",sans-serif}
.hero-copy h1{font-size:27px;line-height:34px;white-space:nowrap}
.hero-copy h2{font-size:27px;line-height:34px;font-weight:400;white-space:nowrap}
.hero-copy em{font-style:normal;color:var(--gold)}
.hero-copy p{font-family:"Arimo",sans-serif;font-size:14px;line-height:19px;margin-top:14px;width:420px}
.btn{display:inline-flex;align-items:center;gap:6px;height:26px;padding:0 12px 0 4px;border-radius:13px;background:linear-gradient(#f6953a,var(--orange-dark));color:var(--white);font-size:11px;font-weight:700}
.btn i{width:18px;height:18px;border-radius:50%;background:var(--white);color:var(--orange);font-style:normal;font-size:11px;text-align:center;line-height:18px}
.hero-copy .btn{margin-top:16px}
.pager{position:absolute;left:952px;top:296px;display:flex;gap:6px}
.pager span{width:20px;height:20px;border-radius:50%;background:var(--white);color:var(--blue-deep);font-size:11px;font-weight:700;text-align:center;line-height:20px}
.pager span.on{background:var(--navy);color:var(--white)}

/* content */
.tabs{position:absolute;left:130px;top:605px;display:flex}
.tabs li{list-style:none;font-size:11px;font-weight:700;padding:5px 14px;border:1px solid var(--line);border-bottom:none;background:#f1f1f1}
.tabs li.on{background:var(--white)}
.welcome{position:absolute;left:130px;top:630px;width:640px;height:290px;border:1px solid var(--line)}
.mini-brand{position:absolute;left:18px;top:18px;display:flex;align-items:center;gap:6px}
.mini-brand .brand-dot{width:24px;height:24px}
.welcome h3{position:absolute;left:60px;top:22px;font-size:24px;font-weight:400;color:var(--navy)}
.welcome h3 b{color:var(--orange);font-weight:400}
.welcome p{position:absolute;left:20px;top:72px;width:360px;font-size:12px;line-height:15px;color:#555}
.team{position:absolute;left:400px;top:72px;width:220px;height:130px;background:linear-gradient(135deg,#c9d6e2,#7f98b0)}
.social{position:absolute;left:20px;top:222px;display:flex;gap:6px}
.social span{width:28px;height:28px;border-radius:4px;background:var(--blue-deep)}
.welcome .btn{position:absolute;right:10px;bottom:6px}
.news{position:absolute;left:800px;top:630px;width:270px;height:290px;border:1px solid var(--line)}
.news h4{position:absolute;left:60px;top:26px;font-size:14px;font-weight:700;color:var(--navy)}
.news .icon{position:absolute;left:18px;top:16px;width:34px;height:34px;border-radius:50%;background:var(--sky)}
.item{position:absolute;left:18px;width:230px;font-size:11px;line-height:14px}
.item .cal{position:absolute;left:0;top:2px;width:26px;height:26px;border-radius:3px;background:var(--blue)}
.item div{margin-left:40px}
.item b{color:var(--navy)}
.item a{color:var(--blue-deep);text-decoration:underline}
.news .btn{position:absolute;right:10px;bottom:6px}

/* footer */
.footer{position:absolute;left:0;top:930px;width:1200px;height:122px;background:linear-gradient(#bfe3f8,var(--sky) 35%,var(--blue-deep))}
.footer .links{position:absolute;left:0;top:48px;width:1200px;text-align:center;font-size:10px;line-height:14px;color:var(--white)}
</style>
</head>
<body>

<header class="wrap header">
  <div class="brand"><span class="brand-dot"></span><span class="brand-name">Dialwell Hub</span></div>
  <div class="utility">Schedule a Demo | IVR Blog | Contact Us | Customer Login <input type="text" aria-label="Search"><span class="go"></span></div>
  <div class="callout"><div class="label">Call us Now: <b>1.800.555.0142</b></div></div>
</header>

<nav class="nav">
  <ul><li>Home</li><li>About Us</li><li>Products</li><li>Services</li><li>Contact Us</li></ul>
  <div class="search">Search here</div>
</nav>

<section class="hero">
  <div class="device" role="img" aria-label="Smartphone with slide-out keyboard showing app icons"></div>
  <div class="hero-copy">
    <h1>Dialwell Hub Services is <em>Different &amp; Better</em></h1>
    <h2>Nullam sed mauris <em>Aliquam consequat vehicula</em></h2>
    <p>Mauris id sodales mi. Aliquam consequat vehicula adipibus ipsum eget convallis quis, euismod vitae lorem. In nonio ipsulipsumer tortor non maesuaulouam consequat vehicula est nun. Ipsum dapibus eget convallis a dapibus semper.</p>
    <span class="btn"><i>›</i>Read More</span>
  </div>
  <div class="pager"><span class="on">1</span><span>2</span><span>3</span><span>4</span></div>
</section>

<ul class="tabs"><li class="on">About Dialwell</li><li>In the News</li><li>Events</li></ul>
<section class="welcome">
  <div class="mini-brand"><span class="brand-dot"></span></div>
  <h3>Welcome to <b>Dialwell Hub!</b></h3>
  <p>Lorem ipsum dolor sit amet, consectetur adipiscing lit. Sed fermentum porttitor velit in bibendum. Nulla facilisiscene leo, vitae cursus ndrao rutrus parturient montesnascetur ndras eget ut sed fermentum adipiscing elit lorem justo porttitor velit in bibendum. Nill in bibendumulla facilisiscene leo, vitae in sed fermentulla facilisis leo, vitae cursus ndras rutrus parturient montes nascetur rulam oded ament fermentum porttitor velitin bibendum leo, vitae min bibendum.</p>
  <div class="team" role="img" aria-label="Photo of a business team in an office"></div>
  <div class="social"><span></span><span></span><span></span><span></span></div>
  <span class="btn"><i>›</i>Read More</span>
</section>

<aside class="news">
  <span class="icon"></span>
  <h4>eNewsletter &amp; Whitepapers</h4>
  <div class="item" style="top:80px"><span class="cal"></span><div><b>May 14, 2011 | Ipsums</b><br>Release of Dialwell Hub<br><a>See the change log</a></div></div>
  <div class="item" style="top:150px"><span class="cal"></span><div><b>May 14, 2011 | Ipsums</b><br>Release of Dialwell Hub<br><a>See the change log</a></div></div>
  <span class="btn"><i>›</i>Read More</span>
</aside>

<footer class="footer">
  <div class="links">
    Home | Products | Services | Contact Us<br>
    100 Sample Street, Suite 200, Springfield ST 00000 | Phone 1.800.555.0142 | Fax 1.800.555.0143<br>
    Solutions | Hosted Voice | Call Routing | Outbound Alerts | Text Notices | Partners | Support<br>
    privacy policy | terms &amp; conditions | site map<br>
    Dialwell hub and the Dialwell name are trademarks of Dialwell Hub. © 2011 All rights reserved.
  </div>
</footer>

</body>
</html>
```